Church Bulletin Ad (see attached sample)

Create a New Church Bulletin Ad. I have attached some samples of what we would like to have in the ad. (1) Marrowfield Realty Quist Logo (2) Headshot (3) Lorna Tavish & Greta Tavish, Real Estate Team (4) Phone number (5) Email address (6) St Agathe Parishioners for over 40 Years. We would like for the ad to be clean and modern. NO OTHER IMAGES besides headshots and Marrowfield Realty Quist Logo.

Target Market(s)

Church community

Industry/Entity Type

Real Estate

Font styles to use
Sans Serif
Other font styles liked:
• Modern Font

Colors
0054AA
0677BA
7BADD7
CADEEF
E8F1F8

Requirements
Must have
• Marrowfield Realty Quist Logo; Headshot; Ad size is 4.5"x1.62"

```html
<!DOCTYPE html>
<html lang="en">
<head>
<meta charset="utf-8">
<title>St Agathe Bulletin Ad – Tavish Real Estate Team</title>
<link rel="stylesheet" href="https://fonts.googleapis.com/css2?family=Lato:wght@400;700&family=Montserrat:wght@800&display=swap">
<style>
  :root {
    --stage: #444243;
    --paper: #ffffff;
    --navy: #16305a;
    --teal: #0677ba;
    --ink: #1a1a1a;
    --photo-light: #e9eef2;
    --photo-mid: #b9aaa0;
    --photo-dark: #2e2a29;
  }
  * { box-sizing: border-box; margin: 0; padding: 0; }
  html, body { width: 1200px; height: 1200px; overflow: hidden; }
  body { background: var(--stage); position: relative; font-family: "Lato", sans-serif; }

  .ad {
    position: absolute; left: 189px; width: 810px; height: 291px;
    background: var(--paper); overflow: hidden;
    box-shadow: 0 10px 24px rgba(0,0,0,0.45);
  }
  .ad--photo-right { top: 232px; }
  .ad--photo-left { top: 688px; }

  .headshots {
    position: absolute; top: 0; height: 100%;
    background: linear-gradient(90deg, var(--photo-dark) 0%, var(--photo-mid) 30%, var(--photo-light) 55%, var(--photo-mid) 75%, var(--photo-dark) 100%);
  }
  .ad--photo-right .headshots { left: 300px; right: 0; }
  .ad--photo-left .headshots { left: 0; width: 540px; }

  .shapes { position: absolute; inset: 0; width: 810px; height: 291px; }

  .brand-mark {
    position: absolute; top: 15px; width: 61px; height: 56px;
    background: var(--navy); color: var(--paper);
    display: flex; align-items: center; justify-content: center; text-align: center;
    font-family: "Lato", sans-serif; font-weight: 700; font-size: 8.5px; line-height: 1.15;
    padding: 4px; box-shadow: 0 1px 3px rgba(0,0,0,0.35);
  }
  .headline {
    position: absolute; color: var(--navy);
    font-family: "Montserrat", sans-serif; font-weight: 800;
    font-size: 23.5px; line-height: 30px; letter-spacing: 0.6px; text-transform: uppercase;
  }
  .team {
    position: absolute; color: var(--paper);
    font-family: "Lato", sans-serif; font-weight: 700; font-size: 18.5px; line-height: 22px;
  }
  .contact { position: absolute; color: var(--ink); font-size: 19.5px; line-height: 25px; }
  .contact li { list-style: none; display: flex; align-items: center; gap: 12px; }
  .contact svg { width: 20px; height: 20px; flex: none; }

  .ad--photo-right .brand-mark { left: 150px; }
  .ad--photo-right .headline { left: 17px; top: 84px; }
  .ad--photo-right .team { left: 17px; top: 156px; }
  .ad--photo-right .contact { left: 18px; top: 221px; }

  .ad--photo-left .brand-mark { left: 576px; top: 14px; }
  .ad--photo-left .headline { left: 434px; top: 76px; }
  .ad--photo-left .team { left: 466px; top: 148px; }
  .ad--photo-left .contact { left: 517px; top: 220px; }
</style>
</head>
<body>

<svg width="0" height="0" style="position:absolute" aria-hidden="true">
  <defs>
    <linearGradient id="stripe-fade" x1="0" y1="0" x2="0" y2="1">
      <stop offset="0" stop-color="#0677ba"/>
      <stop offset="1" stop-color="#16305a"/>
    </linearGradient>
    <symbol id="icon-phone" viewBox="0 0 20 20">
      <circle cx="10" cy="10" r="8.8" fill="none" stroke="#0677ba" stroke-width="1.4"/>
      <path d="M7 5.5c.6-.3 1.1 0 1.4.6l.6 1.3c.2.5 0 .9-.4 1.2l-.5.4c.5 1.2 1.4 2.1 2.6 2.6l.4-.5c.3-.4.8-.5 1.2-.3l1.3.6c.6.3.8.9.5 1.4-.5.9-1.4 1.4-2.4 1.1-2.6-.8-4.5-2.8-5.2-5.3-.3-1 .1-2.6.5-3.1z" fill="#0677ba"/>
    </symbol>
    <symbol id="icon-mail" viewBox="0 0 20 20">
      <rect x="1.5" y="4.5" width="17" height="11" fill="#0677ba"/>
      <path d="M1.5 4.5 10 11l8.5-6.5M1.5 15.5l6-5M18.5 15.5l-6-5" fill="none" stroke="#fff" stroke-width="1.2"/>
    </symbol>
  </defs>
</svg>

<section class="ad ad--photo-right">
  <div class="headshots" role="img" aria-label="Headshot photo of Lorna Tavish and Greta Tavish in front of a bright office window"></div>
  <svg class="shapes" viewBox="0 0 810 291" aria-hidden="true">
    <polygon points="0,0 476,0 302,291 0,291" fill="#fff"/>
    <polygon points="476,0 512,0 336,291 302,291" fill="url(#stripe-fade)"/>
    <polygon points="0,148 388,148 350,211 0,211" fill="#16305a"/>
    <polygon points="810,258 810,291 790,291" fill="#fff"/>
  </svg>
  <div class="brand-mark">Marrowfield Realty Quist</div>
  <h1 class="headline">St Agathe Parishioners<br>for over 40 years.</h1>
  <p class="team">LORNA TAVISH &amp; GRETA TAVISH,<br>Real Estate Team</p>
  <ul class="contact">
    <li><svg><use href="#icon-phone"/></svg>(206) 555 - 0148</li>
    <li><svg><use href="#icon-mail"/></svg>tavishteam@mrquist.com</li>
  </ul>
</section>

<section class="ad ad--photo-left">
  <div class="headshots" role="img" aria-label="Headshot photo of Lorna Tavish and Greta Tavish in front of a bright office window"></div>
  <svg class="shapes" viewBox="0 0 810 291" aria-hidden="true">
    <polygon points="317,0 810,0 810,291 525,291" fill="#fff"/>
    <polygon points="346,37 370,37 525,291 489,291" fill="url(#stripe-fade)"/>
    <polygon points="434,141 810,141 810,203 472,203" fill="#16305a"/>
    <polygon points="0,245 0,291 36,291" fill="#16305a"/>
  </svg>
  <div class="brand-mark">Marrowfield Realty Quist</div>
  <h2 class="headline">St Agathe Parishioners<br>for over 40 years.</h2>
  <p class="team">LORNA TAVISH &amp; GRETA TAVISH,<br>Real Estate Team</p>
  <ul class="contact">
    <li><svg><use href="#icon-phone"/></svg>(206) 555 - 0148</li>
    <li><svg><use href="#icon-mail"/></svg>tavishteam@mrquist.com</li>
  </ul>
</section>

</body>
</html>
```